Tovimbrel business cards

*update*
I don't want you to use the picture from my website, but the colors and the style, geometric and blueish.
I like the idea of big logo in the center like the previous business cards, I also like the website link at the bottom.
Hello, I need to make new business cards for my job, my website is called Tovimbrel and I'm a front end developer.
I'll attach my previous business card so you can understand what I'm looking for, I'll also share my new website design to let you guys understand what is my style/tastes. I'm looking for something better than my old card , modern and really cool.
I would actually stick to the previous one, but I want it to be terrific and maybe with some colors.

```html
<!DOCTYPE html>
<html lang="en">
<head>
<meta charset="utf-8">
<title>Tovimbrel business cards</title>
<link rel="stylesheet" href="https://fonts.googleapis.com/css2?family=Open+Sans:wght@400;600;700&display=swap">
<style>
  :root {
    --navy: #1c3b63;
    --accent: #3f7fd0;
    --paper: #ffffff;
    --stage: #ebe7e2;
    --ink-soft: #4a5a70;
  }
  * { box-sizing: border-box; margin: 0; padding: 0; }
  html, body { width: 1200px; height: 940px; overflow: hidden; }
  body {
    background: var(--stage);
    font-family: "Open Sans", Arial, sans-serif;
    position: relative;
  }
  .card {
    position: absolute;
    top: 315px;
    width: 540px;
    height: 310px;
    overflow: hidden;
    box-shadow: 0 6px 18px rgba(0,0,0,0.15);
  }
  .card--front { left: 40px; background: var(--paper); }
  .card--back { left: 620px; background: var(--navy); }
  .card__shapes { position: absolute; inset: 0; }

  .brand {
    display: flex;
    align-items: center;
    gap: 10px;
    font-weight: 700;
    font-size: 30px;
    letter-spacing: 0.5px;
    white-space: nowrap;
  }
  .brand__square { width: 16px; height: 16px; flex: none; }

  .identity { position: absolute; }
  .identity__name {
    font-weight: 700;
    font-size: 19px;
    letter-spacing: 0.6px;
    text-transform: uppercase;
    margin-top: 22px;
    white-space: nowrap;
  }
  .identity__role { font-size: 12.5px; margin-top: 2px; white-space: nowrap; }

  .card--front .identity { left: 34px; top: 92px; color: var(--navy); }
  .card--front .brand__square { background: var(--navy); }
  .card--front .identity__role { color: var(--ink-soft); }

  .card--back .identity {
    left: 0; right: 0; top: 100px;
    display: flex; flex-direction: column; align-items: center;
    color: #fff;
  }
  .card--back .brand__square { background: #fff; }

  .contacts {
    position: absolute;
    left: 352px;
    right: 14px;
    top: 38px;
    list-style: none;
    color: #fff;
    font-size: 9.5px;
    line-height: 1.45;
  }
  .contacts__item {
    display: flex;
    align-items: center;
    gap: 10px;
    margin-bottom: 14px;
    white-space: nowrap;
  }
  .contacts__icon { width: 20px; height: 20px; flex: none; }
</style>
</head>
<body>

<section class="card card--front" aria-label="Business card front">
  <svg class="card__shapes" viewBox="0 0 540 310" aria-hidden="true">
    <polygon points="345,0 540,0 540,310 300,310" fill="var(--navy)"/>
    <polygon points="300,310 318,200 372,310" fill="var(--accent)"/>
  </svg>

  <div class="identity">
    <div class="brand"><span class="brand__square"></span>Tovimbrel</div>
    <p class="identity__name">Marco Lentari</p>
    <p class="identity__role">Front End Developer &amp; UI Designer</p>
  </div>

  <ul class="contacts">
    <li class="contacts__item">
      <svg class="contacts__icon" viewBox="0 0 20 20" aria-hidden="true">
        <circle cx="10" cy="10" r="10" fill="#fff"/>
        <path d="M7 5.5l1.6 0 .8 2.3-1 .8a6 6 0 0 0 3 3l.8-1 2.3.8v1.6c0 .6-.5 1-1 1A8 8 0 0 1 6 6.5c0-.5.4-1 1-1z" fill="var(--navy)"/>
      </svg>
      <span>+34 600 418 275 (ES)<br>+39 340 51 27 903 (IT WhatsApp)</span>
    </li>
    <li class="contacts__item">
      <svg class="contacts__icon" viewBox="0 0 20 20" aria-hidden="true">
        <circle cx="10" cy="10" r="10" fill="#fff"/>
        <circle cx="10" cy="10" r="5.5" fill="none" stroke="var(--navy)" stroke-width="1.2"/>
        <ellipse cx="10" cy="10" rx="2.3" ry="5.5" fill="none" stroke="var(--navy)" stroke-width="1.1"/>
        <line x1="4.5" y1="10" x2="15.5" y2="10" stroke="var(--navy)" stroke-width="1.1"/>
      </svg>
      <span>info@marcolentari.com<br>www.tovimbrel.it</span>
    </li>
    <li class="contacts__item">
      <svg class="contacts__icon" viewBox="0 0 20 20" aria-hidden="true">
        <circle cx="10" cy="10" r="10" fill="#fff"/>
        <path d="M10 4.5a4 4 0 0 1 4 4c0 3-4 7-4 7s-4-4-4-7a4 4 0 0 1 4-4z" fill="var(--navy)"/>
        <circle cx="10" cy="8.5" r="1.5" fill="#fff"/>
      </svg>
      <span>Pasaje Rosalia Vent Plaza<br>03187 Solvera Spain<br>NIF/VAT X7281L4Q</span>
    </li>
  </ul>
</section>

<section class="card card--back" aria-label="Business card back">
  <div class="identity">
    <div class="brand"><span class="brand__square"></span>Tovimbrel</div>
    <p class="identity__name">Marco Lentari</p>
    <p class="identity__role">Front End Developer &amp; UI Designer</p>
  </div>
</section>

</body>
</html>
```